Company or website name
- The Quillstone Movers and Storage
- Links to the website
- Quillstonehauling.com
- Describe your company and organization and target audience
- Residential and commercial moving and relocation service that needs a website redesign.
- The design should have the following
- I NEED THE WEBSITE TO BE SIMPLE AND STRAIGHT TO THE POINT...MAIN CONCERN IS THAT THEY FILL OUT INFORMATION TO GET QUOTE. SITE EXAMPLE THAT I LIKE IS ( WWW.MYPELDRAN.COM) https://www.orvikhaulage.com/

```html
<!DOCTYPE html>
<html lang="en">
<head>
<meta charset="utf-8">
<title>Quillstone – Get Moving Quote</title>
<link href="https://fonts.googleapis.com/css2?family=Montserrat:wght@400;500;600;700;800&display=swap" rel="stylesheet">
<style>
:root{
  --green:#7ed321;
  --green-dark:#62b218;
  --forest:#44705a;
  --forest-deep:#2f4c39;
  --ink:#1d1d1d;
  --muted:#8a8a8a;
  --soft:#f4f4f4;
  --white:#ffffff;
  --line:#e2e2e2;
}
*{box-sizing:border-box;margin:0;padding:0}
html,body{width:1200px;height:4326px;overflow:hidden}
body{font-family:"Montserrat",sans-serif;color:var(--ink);background:var(--white);position:relative}
.abs{position:absolute}
a{color:inherit;text-decoration:none}

/* HERO */
.hero{left:0;top:0;width:1200px;height:624px;background:linear-gradient(180deg,#5d7a63 0%,#7d9583 45%,#9aa99c 100%)}
.hero-photo{left:0;top:0;width:1200px;height:624px;background:radial-gradient(ellipse at 75% 55%,rgba(220,225,220,.45),transparent 55%),linear-gradient(90deg,rgba(40,70,50,.55),rgba(70,100,80,.25) 60%,rgba(40,70,50,.5))}
.brand{display:flex;align-items:center;gap:8px;color:var(--white)}
.brand-mark{width:16px;height:16px;border-radius:50%;background:var(--white)}
.brand-name{font-weight:700;font-size:24px;line-height:1}
.nav{left:306px;top:34px;display:flex;gap:30px;color:#e8efe9;font-size:15px}
.nav .active{color:var(--white);font-weight:700;border-bottom:2px solid var(--white);padding-bottom:6px}
.phone{left:788px;top:35px;color:#e8efe9;font-size:14px;display:flex;gap:6px;align-items:center}
.btn-quote-top{left:928px;top:26px;width:155px;height:36px;background:var(--green);color:var(--white);font-weight:700;font-size:13px;display:flex;align-items:center;justify-content:center}
.hero-title{left:0;top:246px;width:1200px;text-align:center;color:var(--white);font-weight:800;font-size:52px}
.hero-sub{left:0;top:320px;width:1200px;text-align:center;color:var(--white);font-size:14px}
.quote-panel{left:117px;top:379px;width:966px;height:245px;background:rgba(255,255,255,.9)}
.tab{top:24px;width:65px;height:37px;display:flex;flex-direction:column;align-items:center;justify-content:center;font-size:6px;color:#666;gap:3px}
.tab.on{background:var(--white);box-shadow:0 1px 4px rgba(0,0,0,.15);color:var(--ink)}
.f-label{font-size:9px;color:var(--ink)}
.f-input{height:24px;border:1px solid var(--line);background:var(--white);font-size:9px;color:#aaa;display:flex;align-items:center;justify-content:space-between;padding:0 12px}
.btn-outline{left:57px;top:183px;width:415px;height:30px;border:1px solid var(--green);color:var(--green);font-size:11px;font-weight:700;display:flex;align-items:center;justify-content:center}
.btn-solid{left:497px;top:183px;width:411px;height:30px;background:var(--green);color:var(--white);font-size:11px;font-weight:700;display:flex;align-items:center;justify-content:center}

/* ABOUT */
.about-block{left:35px;top:955px;width:210px;height:223px;background:var(--forest)}
.about-photo{left:64px;top:748px;width:461px;height:393px;background:linear-gradient(135deg,#7d8a73 0%,#c9a77d 35%,#e3d8c8 60%,#dfe3e2 100%)}
.about-title{left:599px;top:748px;width:480px;font-weight:700;font-size:33px;line-height:42px}
.check{left:603px;width:490px;display:flex;gap:26px;align-items:flex-start}
.check p{font-size:12px;color:var(--muted);line-height:16px;width:370px;padding-top:2px}
.more-link{left:912px;top:1146px;color:var(--green-dark);font-weight:600;font-size:15px;border-bottom:2px solid var(--green);padding-bottom:6px}

/* HELP */
.help{left:0;top:1275px;width:1200px;height:935px;background:var(--soft)}
.h2{font-weight:700;font-size:32px}
.help-sub{left:117px;top:1421px;width:360px;font-size:12px;line-height:16px;color:var(--muted)}
.tile{width:313px;height:232px;display:flex;align-items:flex-end;justify-content:center;padding-bottom:30px;color:var(--white);font-weight:700;font-size:20px}
.tile.feature{background:var(--forest);flex-direction:column;justify-content:center;align-items:center;text-align:center;padding:0 40px}
.tile.feature p{font-size:12px;font-weight:500;line-height:19px;margin-top:14px}
.tile.feature span{font-size:12px;font-weight:600;border-bottom:1px solid var(--white);margin-top:12px}
.btn-services{left:475px;top:2074px;width:250px;height:60px;background:var(--green);color:var(--white);font-weight:700;font-size:20px;display:flex;align-items:center;justify-content:center}

/* TESTIMONIALS */
.reviews{left:0;top:2210px;width:1200px;height:483px;background:linear-gradient(180deg,#3e5a49 0%,#4a6a52 50%,#3b5643 100%);overflow:hidden}
.review{top:183px;width:492px;height:181px;background:rgba(255,255,255,.2);padding:26px 38px;color:var(--white)}
.review p{font-size:14px;line-height:20px;width:400px}
.review .who{position:absolute;left:38px;top:124px;display:flex;gap:10px;align-items:center}
.avatar{width:34px;height:34px;border-radius:50%;background:#c9c9c9}
.who small{font-size:10px;display:block}
.who b{font-size:15px}
.stars{position:absolute;right:48px;top:128px;display:flex;gap:6px}
.dot{top:415px;width:20px;height:20px;border-radius:50%;border:2px solid rgba(255,255,255,.8)}
.dot.on::after{content:"";position:absolute;left:3px;top:3px;width:10px;height:10px;border-radius:50%;background:var(--green)}

/* FEATURES */
.feat{width:220px}
.feat h3{font-size:20px;font-weight:700;margin:18px 0 12px}
.feat p{font-size:12px;line-height:17px;color:var(--muted);width:180px}
.feat-hi{left:852px;top:3200px;width:230px;height:200px;background:var(--forest);color:var(--white);padding:18px 14px}
.feat-hi p{color:var(--white)}

/* CTA */
.cta-rule{left:0;top:3689px;width:1200px;height:1px;background:var(--line)}
.cta{left:117px;top:3507px;width:965px;height:235px;background:var(--forest)}
.cta h2{position:absolute;left:64px;top:80px;color:var(--white);font-size:30px;font-weight:700;line-height:42px}
.btn-free{left:601px;top:89px;width:305px;height:59px;background:var(--green);color:var(--white);font-weight:700;font-size:20px;display:flex;align-items:center;justify-content:center}
.partners{left:117px;top:3785px;width:955px;display:flex;justify-content:space-between;align-items:center;color:#555;font-weight:600;font-size:18px}
.partners span{display:flex;align-items:center;gap:8px}
.partners i{width:12px;height:12px;background:#777;display:inline-block}

/* FOOTER */
.footer{left:0;top:3864px;width:1200px;height:462px;background:var(--forest-deep);color:var(--white)}
.foot-text{left:117px;top:143px;width:320px;font-size:16px;line-height:34px}
.socials{left:117px;top:268px;display:flex;gap:12px}
.socials i{width:20px;height:20px;background:var(--green);border-radius:3px;display:block}
.ql{left:616px;top:88px;font-size:20px;font-weight:600}
.ql-links{font-size:16px}
.foot-rule{left:117px;top:344px;width:965px;height:1px;background:rgba(255,255,255,.3)}
.copy{left:0;top:386px;width:1200px;text-align:center;font-size:16px}
</style>
</head>
<body>

<!-- HERO -->
<div class="abs hero"></div>
<div class="abs hero-photo" role="img" aria-label="Moving truck parked by a house in green surroundings"></div>
<div class="abs brand" style="left:117px;top:28px">
  <div class="brand-mark"></div>
  <div class="brand-name">Quillstone</div>
</div>
<nav class="abs nav"><a class="active">Home</a><a>Services</a><a>Offices</a><a>Contact</a></nav>
<div class="abs phone">
  <svg width="14" height="14" viewBox="0 0 24 24" fill="none" stroke="#e8efe9" stroke-width="2"><path d="M22 16.9v3a2 2 0 0 1-2.2 2A19.8 19.8 0 0 1 2.1 4.2 2 2 0 0 1 4.1 2h3a2 2 0 0 1 2 1.7c.1 1 .4 1.9.7 2.8a2 2 0 0 1-.5 2.1L8 9.9a16 16 0 0 0 6 6l1.3-1.3a2 2 0 0 1 2.1-.4c.9.3 1.8.6 2.8.7a2 2 0 0 1 1.7 2z"/></svg>
  +1 555 010 2240
</div>
<a class="abs btn-quote-top">Request A Quote</a>
<h1 class="abs hero-title">GET MOVING QUOTE</h1>
<p class="abs hero-sub">Quillstone is Moving Solutions agent will be e-mailing you a quote in 24 hours or less</p>

<form class="abs quote-panel">
  <div class="abs tab on" style="left:57px"><svg width="14" height="12" viewBox="0 0 24 20"><path d="M12 0 0 10h3v10h6v-6h6v6h6V10h3z" fill="#222"/></svg>Residential</div>
  <div class="abs tab" style="left:152px"><svg width="12" height="12" viewBox="0 0 24 24"><rect x="3" y="2" width="18" height="20" fill="#888"/></svg>Office</div>
  <div class="abs tab" style="left:232px"><svg width="12" height="12" viewBox="0 0 24 24"><rect x="3" y="4" width="18" height="16" fill="#888"/></svg>Storage</div>

  <div class="abs f-label" style="left:57px;top:76px">Full Name*</div>
  <div class="abs f-input" style="left:57px;top:92px;width:271px">Your Full Name</div>
  <div class="abs f-label" style="left:346px;top:76px">Handphone*</div>
  <div class="abs f-input" style="left:346px;top:92px;width:272px">Your Phone Number</div>
  <div class="abs f-label" style="left:636px;top:76px">Email*</div>
  <div class="abs f-input" style="left:636px;top:92px;width:272px">Your Email</div>

  <div class="abs f-label" style="left:57px;top:128px">Moving Date*</div>
  <div class="abs f-input" style="left:57px;top:144px;width:271px">Select a date</div>
  <div class="abs f-label" style="left:346px;top:128px">Moving From*</div>
  <div class="abs f-input" style="left:346px;top:144px;width:272px">Select Zip Code <span style="color:#555">▾</span></div>
  <div class="abs f-label" style="left:636px;top:128px">Moving To*</div>
  <div class="abs f-input" style="left:636px;top:144px;width:272px">Select Zip Code <span style="color:#555">▾</span></div>

  <a class="abs btn-outline">Make Reservation</a>
  <a class="abs btn-solid">Free Quote</a>
</form>

<!-- ABOUT -->
<div class="abs about-block"></div>
<div class="abs about-photo" role="img" aria-label="Person relaxing on a sofa beside stacked moving boxes and a plant"></div>
<h2 class="abs about-title">Safe, Reliable And Express Solutions With Quillstone</h2>

<div class="abs check" style="top:854px"><svg width="37" height="37" viewBox="0 0 36 36" fill="none" stroke="#7ed321" stroke-width="2.5"><path d="M30 18v13H4V5h20"/><path d="M10 16l7 7L33 6"/></svg><p>We're a stress-free moving company. Our goal is to get you moved easily efficiently.</p></div>
<div class="abs check" style="top:906px"><svg width="37" height="37" viewBox="0 0 36 36" fill="none" stroke="#7ed321" stroke-width="2.5"><path d="M30 18v13H4V5h20"/><path d="M10 16l7 7L33 6"/></svg><p>We can handle any job, from one-room apartments to expansive estates.</p></div>
<div class="abs check" style="top:958px"><svg width="37" height="37" viewBox="0 0 36 36" fill="none" stroke="#7ed321" stroke-width="2.5"><path d="M30 18v13H4V5h20"/><path d="M10 16l7 7L33 6"/></svg><p>Our team offers you convenient and affordable options for a completely stress-free experience.</p></div>
<div class="abs check" style="top:1010px"><svg width="37" height="37" viewBox="0 0 36 36" fill="none" stroke="#7ed321" stroke-width="2.5"><path d="M30 18v13H4V5h20"/><path d="M10 16l7 7L33 6"/></svg><p>Our reliable local movers live in the communities they serve. We're not just your movers, we're your neighbors.</p></div>
<div class="abs check" style="top:1080px"><svg width="37" height="37" viewBox="0 0 36 36" fill="none" stroke="#7ed321" stroke-width="2.5"><path d="M30 18v13H4V5h20"/><path d="M10 16l7 7L33 6"/></svg><p>Our trained, professional movers undergo rigorous background checks to maintain quality.</p></div>
<a class="abs more-link">More About Us</a>

<!-- HELP -->
<section class="abs help"></section>
<h2 class="abs h2" style="left:117px;top:1366px">How We Can Help ?</h2>
<p class="abs help-sub">We're a stress-free moving company. Our goal is to get you moved easily efficiently.</p>

<div class="abs tile feature" style="left:117px;top:1510px">Residential<p>Lorem ipsum sit dolor amet della rapisota daeltarso subdiso</p><span>Learn More</span></div>
<div class="abs tile" style="left:445px;top:1510px;background:linear-gradient(180deg,#8a8f86,#4c5a4f)" role="img" aria-label="Office desk with laptop and plants">Office</div>
<div class="abs tile" style="left:770px;top:1510px;background:linear-gradient(180deg,#9e8fa3,#5b5f56)" role="img" aria-label="Warehouse shelves with stored goods and a pallet jack">Storage</div>
<div class="abs tile" style="left:117px;top:1757px;background:linear-gradient(180deg,#7b8179,#3f4a40)" role="img" aria-label="Movers packing kitchen items">Local</div>
<div class="abs tile" style="left:445px;top:1757px;background:linear-gradient(180deg,#8a9a90,#4a5448)" role="img" aria-label="Long straight highway across open land">Long Distance</div>
<div class="abs tile" style="left:770px;top:1757px;background:linear-gradient(180deg,#a9b6b4,#6b5a4c)" role="img" aria-label="Container ship stacked with cargo">Logistic</div>
<a class="abs btn-services">View All Service</a>

<!-- TESTIMONIALS -->
<section class="abs reviews" role="img" aria-label="City skyline at dusk behind client reviews">
  <h2 class="abs h2" style="left:117px;top:94px;color:#fff">What Client Say About Quillstone</h2>
  <div class="abs review" style="left:117px">
    <p>Sales person was the primary reason I choose Quillstone, The driver and his partner were right on top of everything from the packing of the truck to the unloading storage of my goods.</p>
    <div class="who"><div class="avatar"></div><div><small>March 22, 2022</small><b>Harlan P.</b></div></div>
    <div class="stars"><svg width="110" height="18" viewBox="0 0 110 18" fill="#7ed321"><path id="s" d="M9 0l2.6 6 6.4.5-4.9 4.2 1.5 6.3L9 13.6 3.4 17l1.5-6.3L0 6.5 6.4 6z"/><use href="#s" x="23"/><use href="#s" x="46"/><use href="#s" x="69"/><use href="#s" x="92"/></svg></div>
  </div>
  <div class="abs review" style="left:631px">
    <p>Sales person was the primary reason I choose Quillstone, The driver and his partner were right on top of everything from the packing of the truck to the unloading storage of my goods.</p>
    <div class="who"><div class="avatar"></div><div><small>March 22, 2022</small><b>Harlan P.</b></div></div>
    <div class="stars"><svg width="110" height="18" viewBox="0 0 110 18" fill="#7ed321"><use href="#s"/><use href="#s" x="23"/><use href="#s" x="46"/><use href="#s" x="69"/><use href="#s" x="92"/></svg></div>
  </div>
  <div class="abs review" style="left:1145px">
    <p>Sales person was the primary reason I choose Quillstone, The driver and his partner were right on top of everything from the packing of the truck to the unloading storage of my goods.</p>
  </div>
  <div class="abs dot on" style="left:557px"></div>
  <div class="abs dot" style="left:589px"></div>
  <div class="abs dot" style="left:623px"></div>
</section>

<!-- FEATURES -->
<h2 class="abs h2" style="left:117px;top:2782px;line-height:42px;width:420px">Don't Ever Hesitate To Choose Us In Your Goods Moving Service</h2>

<div class="abs feat" style="left:131px;top:2978px"><svg width="48" height="40" viewBox="0 0 48 40" fill="none" stroke="#7ed321" stroke-width="2.2"><circle cx="16" cy="11" r="8"/><path d="M2 38c0-8 6-13 14-13s14 5 14 13"/><path d="M32 26l4 4 8-8"/></svg><h3>Propessional</h3><p>Get moved with our high quality, low cost moving company.</p></div>
<div class="abs feat" style="left:374px;top:2978px"><svg width="48" height="40" viewBox="0 0 48 40" fill="#7ed321"><rect x="4" y="2" width="40" height="26" rx="2"/><rect x="10" y="8" width="28" height="6" fill="#fff"/><rect x="14" y="30" width="6" height="8"/><rect x="28" y="30" width="6" height="8"/></svg><h3>Local</h3><p>Get moved with our experienced and friendly local movers that will have you settled in 24 hours.</p></div>
<div class="abs feat" style="left:621px;top:2978px"><svg width="48" height="40" viewBox="0 0 48 40" fill="none" stroke="#7ed321" stroke-width="2.2"><circle cx="24" cy="8" r="5"/><circle cx="12" cy="12" r="4"/><circle cx="36" cy="12" r="4"/><path d="M17 38V20h14v18M6 34V22h8M42 34V22h-8"/></svg><h3>Reliable</h3><p>You can rest assured that your move will go exactly as planned.</p></div>
<div class="abs feat" style="left:866px;top:2978px"><svg width="48" height="40" viewBox="0 0 48 40" fill="none" stroke="#7ed321" stroke-width="2.2"><rect x="3" y="6" width="40" height="28" rx="3"/><path d="M3 14h40M3 20h40" stroke-width="4"/><path d="M9 28h10"/></svg><h3>Transparent Pricing</h3><p>Get moved with our high quality, low cost moving company.</p></div>

<div class="abs feat" style="left:131px;top:3224px"><svg width="48" height="44" viewBox="0 0 48 48" fill="none" stroke="#7ed321" stroke-width="2.2"><circle cx="24" cy="24" r="21"/><ellipse cx="24" cy="24" rx="9" ry="21"/><path d="M3 24h42"/></svg><h3>Realtime Tracking</h3><p>Get moved with our high quality, low cost moving company.</p></div>
<div class="abs feat" style="left:374px;top:3224px"><svg width="48" height="44" viewBox="0 0 48 48" fill="#7ed321"><path d="M24 2 6 9v13c0 12 8 21 18 24 10-3 18-12 18-24V9z"/><path d="M24 8v32c-7-3-12-10-12-18V13z" fill="#fff"/></svg><h3>Security For Cargo</h3><p>Get moved with our high quality, low cost moving company.</p></div>
<div class="abs feat" style="left:621px;top:3224px"><svg width="48" height="44" viewBox="0 0 48 48" fill="none" stroke="#7ed321" stroke-width="2.2"><circle cx="24" cy="24" r="21"/><path d="M24 34V14M15 22l9-9 9 9"/></svg><h3>Easy Payment</h3><p>Get moved with our high quality, low cost moving company.</p></div>
<div class="abs feat feat-hi"><svg width="48" height="44" viewBox="0 0 48 48" fill="none" stroke="#fff" stroke-width="2.2"><path d="M44 4 4 20l16 6 6 16z"/><path d="M44 4 20 26"/></svg><h3>Fast &amp; Efisient</h3><p>Get moved with our high quality, low cost moving company.</p></div>

<!-- CTA -->
<div class="abs cta-rule"></div>
<div class="abs cta">
  <h2>IS YOUR MOVE RIGHT<br>AROUND THE CORNER?</h2>
  <a class="abs btn-free">Get A Free Quote Today</a>
</div>

<div class="abs partners">
  <span><i></i>MERIDALE</span>
  <span><i></i>Norvane Group</span>
  <span><i></i>Fintrella</span>
  <span><i></i>Quorix Analysts</span>
  <span><i></i>Ascendry</span>
  <span><i></i>dynaro</span>
</div>

<!-- FOOTER -->
<footer class="abs footer">
  <div class="abs brand" style="left:124px;top:94px">
    <div class="brand-mark" style="width:20px;height:20px"></div>
    <div class="brand-name" style="font-size:30px">Quillstone</div>
  </div>
  <p class="abs foot-text">Quillstone is Moving Solutions agent will be e-mailing you a quote in 24 hours or less</p>
  <div class="abs socials"><i></i><i></i><i></i><i></i></div>
  <h4 class="abs ql">Quick Links</h4>
  <a class="abs ql-links" style="left:616px;top:144px">Request A Quote</a>
  <a class="abs ql-links" style="left:787px;top:144px">Track &amp; Trace</a>
  <a class="abs ql-links" style="left:926px;top:144px">Find A Location</a>
  <a class="abs ql-links" style="left:616px;top:186px">Global Agents</a>
  <a class="abs ql-links" style="left:789px;top:186px">Help &amp; FAQ</a>
  <a class="abs ql-links" style="left:930px;top:186px">Careers</a>
  <div class="abs foot-rule"></div>
  <p class="abs copy">Copyright 2022 &nbsp;|&nbsp; Quillstone</p>
</footer>

</body>
</html>
```